Business Card Design Project for Harbourlight Homes

We need a business card design for Harbourlight Homes Ltd, a respected building company that specialises in high quality designer homes.

We're after a sleek, clean, modern business card (could even have an interesting shape or something different from normal business cards) with wow factor that people will remember. It also needs to look sharp and great on print.

Please see example attached (do not copy, for inspiration only).

It needs to be in line with the new logo (see attached) and look consistent with that.

The new business card should include the Trusted Trades logo (see attached) as well as the company logo and the two need to look balanced and sleek in regards to their position on the card.
_______________________________________________________
Details to be included:
Tobin Vareck
Director

M: 021 555 0148
E: milo@harbourlighthomes.example
W: www.harbourlighthomes.example

If you present an option for an open card, here's some additional wording we would like you to use:

Harbourlight Homes are a highly skilled team who specialises in residential projects, from simple homes through to top end architectural designs.
We will treat your project with integrity, the attention it deserves, and we guarantee 100% satisfaction.

Timeless craftsmanship. Uncompromising standards.

___________________________________________________________
Additional info on Harbourlight Homes for your consideration:

The core values of the company are integrity, trust, expertise and uncompromising standards.

Harbourlight Homes have been building homes for over 20 years. Only residential, from simple 2-3 bedroom homes through to top end architectural designs. They are a registered Trusted Trade (the Trusted Trades Federation is a highly trusted and respected organisation in New Zealand).

The team at Harbourlight Homes pride themselves in delivering impeccable service to their clients and position themselves as their trusted partners and friends in the construction of their most valuable asset.

Thanks! We look forward to your designs!!!

Target Market(s)

People 30 yrs+ who have an interest in owning quality homes and are prepared to pay for it. Homes built to standards, future-proofed, building savvy.

Industry/Entity Type

Construction

Requirements
Must have
• We're looking for some wow factor as well and something that stands out and people will remember

The final design should communicate timeless craftsmanship, trust, special, VALUE, exquisite, stylish, standing the test of time, no cutting corners, reliability and high standards.

The final design also needs to be sharp and look great on print. The file supplied needs to be high resolution.

```html
<!DOCTYPE html>
<html lang="en">
<head>
<meta charset="utf-8">
<title>Harbourlight Homes – Key Business Card</title>
<link rel="stylesheet" href="https://fonts.googleapis.com/css2?family=Marcellus&display=swap">
<style>
  :root {
    --page: #f4f4f4;
    --card-sky: #bcd8f6;
    --key-gold: #fbd84a;
    --key-white: #ffffff;
    --ink: #111111;
    --badge-blue: #1c3f8a;
    --brand-red: #d2232a;
    --tool-dark: #1d1d1d;
  }
  * { margin: 0; padding: 0; box-sizing: border-box; }
  html, body {
    width: 1200px;
    height: 959px;
    overflow: hidden;
    background: var(--page);
  }
  .sheet { position: relative; width: 1200px; height: 959px; }
  .card {
    position: absolute;
    width: 450px;
    height: 260px;
    display: block;
  }
  .card--front-gold  { left: 92px;  top: 130px; }
  .card--front-white { left: 632px; top: 130px; }
  .card--back-contact{ left: 92px;  top: 546px; }
  .card--back-brand  { left: 632px; top: 546px; }

  .card-ground { fill: var(--card-sky); }
  .key-outline {
    stroke: var(--ink);
    stroke-width: 2.4;
    stroke-dasharray: 8 5;
    stroke-linejoin: round;
  }
  .key--gold  { fill: var(--key-gold); }
  .key--white { fill: var(--key-white); }
  .cut-tool { fill: var(--tool-dark); }

  .role-title, .person-name, .contact-line, .brand-name {
    font-family: "Marcellus", "Times New Roman", serif;
    fill: var(--ink);
  }
  .role-title  { font-size: 11px; }
  .person-name { font-size: 25px; letter-spacing: 0.5px; }
  .contact-line { font-size: 16.5px; }
  .brand-name { font-size: 10px; letter-spacing: 0.3px; }
  .brand-name--large { font-size: 19px; letter-spacing: 0.8px; }
  .partner-badge { fill: var(--badge-blue); }
  .brand-square { fill: var(--brand-red); }
</style>
</head>
<body>
<main class="sheet">

  <!-- Front, gold key -->
  <svg class="card card--front-gold" viewBox="0 0 375 217" aria-label="Business card front, gold key">
    <defs>
      <path id="key-shape" d="M170,8 C110,-5 20,5 5,100 C0,180 60,217 120,215 C160,214 170,190 175,158 L195,150 L210,162 L222,148 L240,165 L255,150 L272,160 L290,140 L330,140 L342,150 L365,130 L375,110 L355,60 L172,60 C176,40 176,20 170,8 Z"/>
    </defs>
    <rect class="card-ground" width="375" height="217"/>
    <use href="#key-shape" class="key-outline key--gold"/>
    <rect class="cut-tool" x="172" y="30" width="122" height="32" rx="14" role="img" aria-label="Scissors cutting along the dashed key outline"/>
    <text class="role-title" x="178" y="88">director</text>
    <text class="person-name" x="355" y="112" text-anchor="end">TOBIN</text>
    <text class="person-name" x="352" y="140" text-anchor="end">VARECK</text>
  </svg>

  <!-- Front, white key -->
  <svg class="card card--front-white" viewBox="0 0 375 217" aria-label="Business card front, white key">
    <rect class="card-ground" width="375" height="217"/>
    <use href="#key-shape" class="key-outline key--white"/>
    <rect class="cut-tool" x="172" y="30" width="122" height="32" rx="14" role="img" aria-label="Scissors cutting along the dashed key outline"/>
    <text class="role-title" x="178" y="88">director</text>
    <text class="person-name" x="355" y="112" text-anchor="end">TOBIN</text>
    <text class="person-name" x="352" y="140" text-anchor="end">VARECK</text>
  </svg>

  <!-- Back, contact details -->
  <svg class="card card--back-contact" viewBox="0 0 375 217" aria-label="Business card back with contact details">
    <rect class="card-ground" width="375" height="217"/>
    <use href="#key-shape" class="key-outline key--white" transform="translate(375,0) scale(-1,1)"/>
    <rect class="cut-tool" x="80" y="32" width="122" height="32" rx="14" role="img" aria-label="Scissors cutting along the dashed key outline"/>
    <rect class="partner-badge" x="210" y="48" width="24" height="28"/>
    <rect class="brand-square" x="240" y="52" width="12" height="12"/>
    <text class="brand-name" x="256" y="60">HARBOURLIGHT</text>
    <text class="brand-name" x="256" y="72">HOMES LTD</text>
    <text class="contact-line" x="28" y="104">E: milo@harbourlighthomes.example</text>
    <text class="contact-line" x="28" y="126">W: www.harbourlighthomes.example</text>
    <text class="contact-line" x="352" y="150" text-anchor="end">M: 021 555 0148</text>
  </svg>

  <!-- Back, brand marks -->
  <svg class="card card--back-brand" viewBox="0 0 375 217" aria-label="Business card back with company and partner marks">
    <rect class="card-ground" width="375" height="217"/>
    <use href="#key-shape" class="key-outline key--white" transform="translate(375,0) scale(-1,1)"/>
    <rect class="partner-badge" x="45" y="65" width="63" height="65"/>
    <rect class="brand-square" x="140" y="76" width="36" height="36"/>
    <text class="brand-name brand-name--large" x="186" y="92">HARBOURLIGHT</text>
    <text class="brand-name brand-name--large" x="186" y="114">HOMES LTD</text>
  </svg>

</main>
</body>
</html>
```